new Tavrin Care flyer

Redesign our flyer completely. A copy of our current flyers are attached (which are being combined into 1). Use anything from these that u want.
It's given to patients with a whole lot of flyers from our competitors - so needs to stand out
Essential elements are:
1. Text: $99 CPAP Trial (prominent - this is the main point of the flyer)
- Our all inclusive 4 week CPAP or APAP trial includes everything you need to get started for just $99. Plus we'll refund your trial fee when you're ready to buy your own machine.
2. Text: Proudly Independent! (keep this separate from themain promotion.
- Many CPAP clinics in Victoria are now owned by one or other of the big CPAP manufacturers; while many others only stock one brand. We stock all the leading brands and offer genuinely independent advice and friendly service.
3. Text: Call us for an appointment
- Ashburton (03) 9412 6083 5/418 Dorran Street (suburb and phone prominent)
- Brighton (03) 9263 5540 27b Tamsley Grove (suburb and phone prominent)
- Kew East (03) 9351 2874 2637 Fennick Road (suburb and phone prominent)
4. Our logo - attached
5. small supplier logos grouped together - corvane, talvix, morrow&dunlee - attached
6. images for background / filler - talvix machine, mdh machine - attached, must use at least one of talvix pics

```html
<!DOCTYPE html>
<html lang="en">
<head>
<meta charset="utf-8">
<title>Tavrin Care flyer</title>
<link href="https://fonts.googleapis.com/css2?family=Roboto+Condensed:wght@400;700&family=Asap+Condensed:wght@400;500;600&display=swap" rel="stylesheet">
<style>
  :root {
    --green: #7cbf3a;
    --green-dark: #5fa32a;
    --grey: #8c8c8c;
    --grey-dark: #555;
    --text: #4a4a4a;
    --navy: #1e3a78;
    --page: #ecece8;
    --white: #ffffff;
    --band-light: #f3f9e6;
    --band-mid: #c9e69a;
  }
  * { box-sizing: border-box; margin: 0; padding: 0; }
  html, body { width: 1200px; height: 1000px; overflow: hidden; }
  body { background: var(--page); font-family: "Asap Condensed", "Arial Narrow", sans-serif; color: var(--text); position: relative; }

  .flyer { position: absolute; top: 30px; width: 450px; height: 940px; background: var(--white); overflow: hidden; box-shadow: 0 3px 12px rgba(0,0,0,.15); }
  .flyer--front { left: 140px; }
  .flyer--back { left: 610px; }
  .abs { position: absolute; }

  .band { position: absolute; left: 0; right: 0;
    background: radial-gradient(circle at 30% 40%, var(--band-light) 0%, transparent 45%),
                radial-gradient(circle at 80% 70%, #eef7dc 0%, transparent 40%),
                linear-gradient(180deg, var(--band-mid) 0%, #e6f3cf 55%, var(--band-light) 100%); }
  .band--bottom { background: radial-gradient(circle at 70% 30%, var(--band-light) 0%, transparent 45%),
                linear-gradient(180deg, var(--band-mid) 0%, #e8f4d3 40%, var(--white) 100%); }
  .dotted { position: absolute; left: 0; right: 0; border-top: 2px dotted var(--green); }

  .logo { position: absolute; left: 0; right: 0; text-align: center; font-family: "Roboto Condensed", sans-serif; font-weight: 400; font-size: 62px; letter-spacing: 1px; color: var(--green); line-height: 1; }

  .photo { position: absolute; }
  .photo--talvix { left: 130px; top: 205px; width: 300px; height: 150px; border-radius: 8px; background: linear-gradient(135deg, #2a2a2a 0%, #111 55%, #d9dcdf 56%, #f4f5f6 100%); box-shadow: 0 10px 16px rgba(0,0,0,.2); }
  .photo--mdh { left: 60px; top: 490px; width: 390px; height: 200px;
    clip-path: polygon(69% 0, 100% 0, 100% 100%, 0 100%, 0 65%, 69% 65%);
    background: linear-gradient(160deg, #3a3a3a 0%, #1d1d1d 45%, #8a7a6a 70%, #c9c2b8 100%); }

  .price { left: 60px; top: 372px; display: flex; align-items: flex-start; }
  .price__dollar { font-family: "Roboto Condensed", sans-serif; font-weight: 700; font-size: 34px; color: var(--grey); margin-top: 18px; }
  .price__amount { font-family: "Roboto Condensed", sans-serif; font-weight: 700; font-size: 128px; line-height: 1; color: var(--grey); letter-spacing: -4px; }
  .price__label { margin-left: 12px; margin-top: 16px; font-family: "Roboto Condensed", sans-serif; font-weight: 700; font-size: 42px; line-height: 1; }
  .price__label .cpap { color: var(--green); display: block; padding-bottom: 6px; border-bottom: 2px dotted var(--green); }
  .price__label .trial { color: var(--grey); display: block; padding-top: 4px; }

  .lede { left: 30px; right: 30px; top: 522px; text-align: center; font-size: 14px; line-height: 1.4; color: var(--text); }
  .lede p + p { margin-top: 6px; }

  .cta { left: 0; right: 0; text-align: center; font-weight: 500; color: var(--green-dark); }
  .cta--front { top: 648px; font-size: 27px; }

  .offices { left: 30px; right: 30px; top: 700px; display: flex; justify-content: space-around; }
  .office__suburb { font-family: "Roboto Condensed", sans-serif; font-weight: 700; font-size: 18px; color: var(--green-dark); text-transform: uppercase; }
  .office__phone { display: flex; align-items: center; gap: 5px; font-family: "Roboto Condensed", sans-serif; font-size: 17px; color: var(--grey-dark); }
  .icon-phone { width: 12px; height: 12px; fill: currentColor; }

  .independent { left: 40px; right: 40px; top: 778px; text-align: center; }
  .independent h2 { font-family: "Roboto Condensed", sans-serif; font-weight: 700; font-size: 18px; color: var(--green-dark); letter-spacing: .5px; }
  .independent p { margin-top: 6px; font-size: 12.5px; line-height: 1.45; color: var(--text); }

  .suppliers { left: 20px; right: 20px; display: flex; justify-content: space-between; align-items: center; font-weight: 600; font-size: 17px; }
  .suppliers--front { top: 880px; }
  .suppliers--back { top: 882px; }
  .supplier { color: var(--navy); }

  .cta--back { top: 190px; font-family: "Roboto Condensed", sans-serif; font-weight: 700; font-size: 17px; letter-spacing: .5px; }
  .location { position: absolute; left: 40px; right: 20px; display: flex; gap: 14px; }
  .location__map { width: 160px; height: 118px; background: linear-gradient(135deg, #e3e3e3, #c9c9c9); flex: none; }
  .location__suburb { font-family: "Roboto Condensed", sans-serif; font-weight: 700; font-size: 22px; color: var(--grey); text-transform: uppercase; margin-top: 4px; }
  .location__address { font-size: 11px; color: var(--grey-dark); }
  .location__phone { display: flex; align-items: center; gap: 6px; margin-top: 6px; font-family: "Roboto Condensed", sans-serif; font-weight: 700; font-size: 18px; color: var(--green-dark); }

  .tagline { left: 0; right: 0; top: 715px; text-align: center; font-weight: 500; font-size: 26px; color: var(--green-dark); }
  .hours { left: 0; right: 0; top: 768px; text-align: center; font-size: 14px; line-height: 1.7; color: var(--text); }
  .hours h3 { font-family: "Roboto Condensed", sans-serif; font-weight: 700; font-size: 13px; color: var(--green-dark); letter-spacing: .5px; }
  .hours .contact { color: var(--green-dark); font-weight: 500; margin-top: 4px; }
</style>
</head>
<body>
<svg width="0" height="0" style="position:absolute">
  <symbol id="phone" viewBox="0 0 24 24"><path d="M6.6 10.8a15.1 15.1 0 0 0 6.6 6.6l2.2-2.2a1 1 0 0 1 1-.25 11.4 11.4 0 0 0 3.6.57 1 1 0 0 1 1 1V20a1 1 0 0 1-1 1A17 17 0 0 1 3 4a1 1 0 0 1 1-1h3.5a1 1 0 0 1 1 1c0 1.25.2 2.45.57 3.57a1 1 0 0 1-.25 1z"/></symbol>
</svg>

<section class="flyer flyer--front">
  <div class="band" style="top:0;height:335px"></div>
  <div class="dotted" style="top:335px"></div>
  <div class="logo" style="top:100px">TAVRINCARE</div>
  <div class="photo photo--talvix" role="img" aria-label="Talvix CPAP machine with colour screen and water chamber"></div>

  <div class="abs price">
    <span class="price__dollar">$</span>
    <span class="price__amount">99</span>
    <span class="price__label"><span class="cpap">CPAP</span><span class="trial">TRIAL</span></span>
  </div>

  <div class="abs lede">
    <p>Our all inclusive 4 week CPAP or APAP trial includes everything you need to get started for just $99.</p>
    <p>Plus we’ll refund your trial fee when you’re ready to buy your own machine.</p>
  </div>

  <div class="band band--bottom" style="top:622px;bottom:0"></div>
  <div class="dotted" style="top:622px"></div>
  <div class="abs cta cta--front">Call us for an appointment</div>

  <div class="abs offices">
    <div class="office"><div class="office__suburb">Ashburton</div><div class="office__phone"><svg class="icon-phone"><use href="#phone"/></svg>9412 6083</div></div>
    <div class="office"><div class="office__suburb">Brighton</div><div class="office__phone"><svg class="icon-phone"><use href="#phone"/></svg>9263 5540</div></div>
    <div class="office"><div class="office__suburb">Kew East</div><div class="office__phone"><svg class="icon-phone"><use href="#phone"/></svg>9351 2874</div></div>
  </div>

  <div class="abs independent">
    <h2>PROUDLY INDEPENDENT</h2>
    <p>Many CPAP clinics in Victoria are now owned by one or other of the big CPAP manufacturers; while many others only stock one brand. We stock all the leading brands and offer genuinely independent advice and friendly service.</p>
  </div>

  <div class="abs suppliers suppliers--front">
    <span class="supplier">Morrow&amp;Dunlee</span>
    <span class="supplier">Corvane Haldrix</span>
    <span class="supplier">Talvix</span>
  </div>
</section>

<section class="flyer flyer--back">
  <div class="band" style="top:0;height:90px"></div>
  <div class="dotted" style="top:90px"></div>
  <div class="logo" style="top:118px">TAVRINCARE</div>
  <div class="abs cta cta--back">CALL US FOR AN APPOINTMENT</div>

  <div class="location" style="top:220px">
    <div class="location__map" role="img" aria-label="Street map of the Ashburton clinic"></div>
    <div><div class="location__suburb">Ashburton</div><div class="location__address">5/418 Dorran Street</div>
      <div class="location__phone"><svg class="icon-phone"><use href="#phone"/></svg>9412 6083</div></div>
  </div>
  <div class="location" style="top:350px">
    <div class="location__map" role="img" aria-label="Street map of the Brighton clinic"></div>
    <div><div class="location__suburb">Brighton</div><div class="location__address">27b Tamsley Grove</div>
      <div class="location__phone"><svg class="icon-phone"><use href="#phone"/></svg>9263 5540</div></div>
  </div>
  <div class="photo photo--mdh" role="img" aria-label="Morrow&amp;Dunlee CPAP machine on a bedside table"></div>
  <div class="location" style="top:480px">
    <div class="location__map" role="img" aria-label="Street map of the Kew East clinic"></div>
    <div><div class="location__suburb">Kew East</div><div class="location__address">2637 Fennick Road</div>
      <div class="location__phone"><svg class="icon-phone"><use href="#phone"/></svg>9351 2874</div></div>
  </div>

  <div class="band band--bottom" style="top:690px;bottom:0"></div>
  <div class="dotted" style="top:690px"></div>
  <div class="abs tagline">If you can’t sleep, neither can we</div>
  <div class="abs hours">
    <h3>APPOINTMENT HOURS</h3>
    <div>Monday to Friday 7am–7pm</div>
    <div>Saturday 10am–2pm</div>
    <div class="contact">info@tavrincare.com.au &nbsp;|&nbsp; www.tavrincare.com.au</div>
  </div>
  <div class="abs suppliers suppliers--back">
    <span class="supplier">Morrow&amp;Dunlee</span>
    <span class="supplier">Corvane Haldrix</span>
    <span class="supplier">Talvix</span>
  </div>
</section>
</body>
</html>
```